Web Site Upgrade. Word Press Design.

Trimora Pty Ltd
www.trimora.com.au
Australia
Please see below design requirements for re-branding and renaming the Trimora Pty. Ltd. To the new site to “Bistro Seating Hub” Chairs + Bar Stools + More:
url: www.bistroseatinghub.com.au Already registered and hosting in place.
• Incorporate new logo in to site. (supplied in various formats including Adobe Illustrator)
• This will need to be Trimora trading as (T/A) “Bistro Seating Hub” Chairs + Bar Stools + More. Using Trimora ABN as shown on current site.
• Redesign template to reflect new colour scheme. To be decided
• Provide a maximum of three PDF concepts for a new design and a minimum of two.
• Redesign home page text, graphics, photos Etc. To make it more appealing to visitors. Points to remember here are:
• Our market is Cafe and Restaurant owners. Not the general public.
• Trimora tables are our own design for which we won the VRN’s Bright Makers.
• Existing site is done in Word Press.
• Web hosting has already been orgainsed with Harbourline Hosting so it will be a case of uploading new site to existing host.
• Create a redirect to new site from old Trimora Site.
• Check all pages check for any SEO issues.
Other than the changes made to the home page template which will be reflected in the rest of the pages, the rest of the site will remain unchanged for the time being.
Target Market(s)
Cafe and Restaurant owners
Industry/Entity Type
Cafe
Requirements
Must have
- Incorporate images of products sold on web site.
Maintain functionality of existing site
Not 100% committed to new logo. Happy to see other suggestions.
Nice to have
- Really friendly SEO properties.
Design to make people go further than the home page and stay on the site
Should not have
- Too cluttered a look.

```html
<!DOCTYPE html>
<html lang="en">
<head>
<meta charset="utf-8">
<title>Bistro Seating Hub – Café Furniture</title>
<link href="https://fonts.googleapis.com/css2?family=Open+Sans:wdth,wght@75,300;100,400;100,600&family=Quicksand:wght@500&family=Arimo:ital,wght@0,400;0,700;1,400&display=swap" rel="stylesheet">
<style>
:root{
  --orange:#f0634a;
  --orange-soft:#f27a62;
  --charcoal:#4a4a4a;
  --grey:#8e8e8e;
  --ink:#2b2b2b;
  --navy:#1c2733;
  --rule:#e3e3e3;
  --white:#ffffff;
}
*{margin:0;padding:0;box-sizing:border-box}
html,body{width:967px;height:1200px;overflow:hidden;background:var(--white)}
body{position:relative;font-family:'Arimo',Arial,sans-serif;color:var(--ink)}
.abs{position:absolute}
.cond{font-family:'Open Sans',sans-serif;font-stretch:75%;font-weight:300}
.round{font-family:'Quicksand',sans-serif;font-weight:500}

.brand{left:84px;top:52px}
.brand-name{position:absolute;left:0;top:0;white-space:nowrap;font-family:'Open Sans',sans-serif;font-weight:600;font-size:30px;line-height:36px;color:#2a3644;letter-spacing:-.5px}
.brand-tag{position:absolute;left:2px;top:40px;white-space:nowrap;font-family:'Open Sans',sans-serif;font-size:15px;line-height:18px;letter-spacing:1.5px;color:#555}
.brand-tag b{color:var(--orange);font-weight:400}

.call{right:90px;top:12px;font-size:27px;line-height:32px;color:var(--ink);white-space:nowrap}
.call span{color:var(--orange)}
.mail{right:90px;top:48px;font-size:11px;color:var(--ink)}
.mail span{color:var(--orange)}
.brochure{left:706px;top:70px;width:174px;height:37px;background:var(--orange);border-radius:4px;overflow:hidden;color:var(--white);font-size:19px;line-height:37px;padding-left:38px;white-space:nowrap}
.brochure i{position:absolute;left:0;top:0;width:32px;height:37px;background:var(--navy)}

.nav{left:84px;top:125px;width:796px;height:38px;border-top:1px solid var(--rule);border-bottom:1px solid var(--rule);font-family:'Open Sans',sans-serif;font-size:14px;color:var(--ink)}
.nav a{position:absolute;top:0;line-height:36px;color:inherit;text-decoration:none;white-space:nowrap}
.nav .current{left:2px;top:4px;width:76px;height:33px;line-height:33px;text-align:center;background:var(--orange);color:var(--white);border-radius:4px 4px 0 0}

.hero{left:85px;top:168px;width:795px;height:276px;border:1px solid var(--rule)}
.hero h1{position:absolute;left:14px;top:12px;font-size:55px;line-height:64px;color:#333}
.hero p{position:absolute;left:18px;top:76px;width:390px;font-size:26px;line-height:32px;color:#444}
.video-btn{position:absolute;left:20px;top:192px;width:208px;height:41px;background:var(--orange);color:var(--white);font-size:22px;line-height:41px;text-align:center;border-radius:3px;box-shadow:0 4px 4px -2px rgba(0,0,0,.35)}
.hero-photo{position:absolute;left:420px;top:22px;width:336px;height:252px;background:radial-gradient(ellipse at 50% 45%,#8a5a44 0,#b9b9b9 45%,#ffffff 75%)}

.col-title{top:452px;font-size:19px;color:#333;font-family:'Open Sans',sans-serif}
.tile{top:485px;height:137px;color:var(--white);padding:12px 12px}
.tile h3{font-size:18px;font-weight:400;margin-bottom:8px}
.tile p{font-size:12px;line-height:14px}
.tile p big{font-size:19px;font-weight:700}
.tile .btn{position:absolute;right:12px;bottom:12px;width:116px;height:28px;background:var(--white);color:var(--ink);font-size:13px;line-height:28px;text-align:center;border-radius:4px}
.t1{left:86px;width:260px;background:var(--charcoal)}
.t2{left:355px;width:258px;background:var(--orange-soft)}
.t3{left:622px;width:258px;background:var(--grey)}

.why{left:92px;top:638px;font-size:26px;color:#333}
.copy{left:92px;top:682px;width:558px;font-size:10.2px;line-height:14.6px;color:#333}
.copy p{margin-bottom:14px}
.copy .shout{font-style:italic;text-transform:uppercase;font-size:10.4px}

.ask{left:672px;top:646px;width:208px;height:108px;border:1px solid var(--rule)}
.ask h4{position:absolute;left:12px;top:8px;font-size:22px;line-height:27px;font-weight:400;color:#333}
.ask-photo{position:absolute;right:0;top:0;width:70px;height:76px;background:linear-gradient(135deg,#f1efec,#d8c3b5)}
.ask-bar{position:absolute;left:0;bottom:0;width:206px;height:31px;background:var(--orange);color:var(--white);font-size:19px;line-height:31px;padding-left:10px}

.testi{left:672px;top:778px;font-size:19px;color:#333}
.bubble{left:672px;top:807px;width:210px;height:141px;background:var(--orange);border-radius:4px;color:var(--white);padding:11px 10px;font-size:10.6px;line-height:13px;font-style:italic}
.bubble:after{content:"";position:absolute;right:44px;bottom:-10px;border-left:10px solid transparent;border-right:10px solid transparent;border-top:10px solid var(--orange)}
.by{left:672px;width:196px;text-align:right;top:967px;font-size:11px;font-style:italic}
.from{left:672px;width:196px;text-align:right;top:986px;font-size:11px;color:#7a3a2e}

.foot-rule{left:0;top:1018px;width:967px;border-top:1px solid var(--rule)}
.fcol{top:1029px;font-size:10.8px;line-height:13.6px;color:#333}
.fcol h5{font-size:13px;font-weight:400;color:var(--orange);margin-bottom:7px}
.fcol span{color:var(--orange)}
.pay{left:679px;top:1052px;width:215px;height:53px;border:1px solid #b9b9b9;border-radius:5px;display:flex;gap:5px;align-items:center;padding:10px 6px 0}
.pay i{flex:1;height:30px;border:1px solid #999;background:#f1f1f1}
.pay i:first-child{background:#d8453a}
.pay i:nth-child(2){background:#f5f5f5}
.pay i:nth-child(3){background:#f6a04a}
.pay i:last-child{background:#3b85c6}
.pay b{position:absolute;left:14px;top:-8px;width:52px;height:15px;background:var(--white);border:1px solid #b9b9b9;border-radius:3px}

.bottom{left:0;top:1150px;width:967px;height:50px;background:var(--navy);color:var(--white);font-size:11px}
.bottom .copyright{position:absolute;left:101px;top:18px}
.bottom .follow{position:absolute;left:754px;top:16px;font-size:13px}
.bottom .soc{position:absolute;top:12px;width:25px;height:25px;border-radius:4px;background:#6f7c88}
</style>
</head>
<body>

<div class="abs brand">
  <div class="brand-name">Bistro Seating Hub</div>
  <div class="brand-tag">Chairs <b>+</b> Bar Stools <b>+</b> More</div>
</div>

<div class="abs call cond"><span>Call us:</span> 0412 880 316</div>
<div class="abs mail"><span>email:</span>admin@trimora.com.au</div>
<div class="abs brochure cond"><i></i>Download a Brochure</div>

<nav class="abs nav">
  <a class="current">Home</a>
  <a style="left:98px">Cafe tables</a>
  <a style="left:202px">Table Bases</a>
  <a style="left:314px">Table Tops</a>
  <a style="left:421px">Cafe Chairs</a>
  <a style="left:533px">Bar Stools</a>
  <a style="left:634px">Blog</a>
  <a style="left:695px">Contact Us</a>
</nav>

<section class="abs hero">
  <h1 class="cond">Café Furniture</h1>
  <p class="cond">Introducing a unique adjustable and stable base, your café table won’t rock or roll, even on unlevel surfaces</p>
  <div class="video-btn cond">WATCH PRODUCT VIDEO</div>
  <div class="hero-photo" role="img" aria-label="Square café table with timber top on a chrome base, with four brown bentwood chairs"></div>
</section>

<div class="abs col-title" style="left:92px">Featured Product</div>
<div class="abs col-title" style="left:360px">Table and Chair Combos</div>
<div class="abs col-title" style="left:626px">Stock Clearance</div>

<div class="abs tile t1">
  <h3>WINNER</h3>
  <p>VRN’s Bright Makers Program <big>2013</big><br>Our featured product, the fully adjustable cafe table base.</p>
  <div class="btn">TAKE A LOOK</div>
</div>
<div class="abs tile t2">
  <h3>LOREM IPSUM DOLOR</h3>
  <p>Suspendisse tempus felis nec lacus biben-<br>dum, in vehicula purus feugiat.</p>
  <div class="btn">VIEW ALL</div>
</div>
<div class="abs tile t3">
  <h3>STOCK CLEARANCE SALE</h3>
  <p>Genuine Stock Clearance Sale on Tables. Table Base were $94.00 ea. Now only $55 ea. plus GST</p>
  <div class="btn">LEARN MORE</div>
</div>

<h2 class="abs why round">Why Buy From Us</h2>
<div class="abs copy">
  <p>A key difference with the design of our cafe tables is the column inserts into the base and table top support by about 50mm with a four point fastening system, it doesn’t just sit on top like other table bases. This makes these table pedestals super strong and unlike all the other cafe table bases, if the fastenings do loosen over time, Trimora table bases stay rock steady. That’s our promise. The Trimora range of award winning table bases includes the Lunara 720mm high base and the Brava 1040 bar height table bases. Both table bases come with the patented adjustment system located high up in the column away from dirt, grime and other nasties. This greatly minimises the risk of damage from feet or chair legs; to either the customer or the tables.</p>
  <p>&nbsp;Many of the best Restaurants and Hotels around Australia are making the switch because, when it comes to real value for money, the Trimora cafe tables are unbeatable.</p>
  <p>The Trimora quality range of cafe tables and chairs, bar stool and table tops is designed to suit every situation yet at an affordable price. Our stylish well priced range of cafe furniture has stood the test of time, and customers.</p>
  <p class="shout">&nbsp;It doesn’t matter if you are just starting out or refurbishing your existing furniture, you simply can’t go wrong with this one.</p>
  <p class="shout">Just add table tops and chairs from our great range to your Trimora cafe table bases , and you’re ready to go .</p>
</div>

<aside class="abs ask">
  <h4 class="round">Have any<br>Questions?</h4>
  <div class="ask-photo" role="img" aria-label="Customer service assistant wearing a headset"></div>
  <div class="ask-bar round">Call us: 0412 880 316</div>
</aside>

<div class="abs testi round">Testimonials</div>
<blockquote class="abs bubble">The result is magnificent!&nbsp; We’re so excited we’d like to share and have attached a photo for you.&nbsp; We have a polished concrete floor and as you know and we discovered – it is notoriously unlevel.&nbsp; Problem solved with Trimora, couldn’t believe how easy and efficient they are.</blockquote>
<div class="abs by">Marlene</div>
<div class="abs from">From Harwood Lane Patisserie</div>

<div class="abs foot-rule"></div>
<div class="abs fcol" style="left:98px">
  <h5>Browse</h5>Cafe tables<br>Table Bases<br>Table Tops<br>Cafe Chairs<br>Bar Stools
</div>
<div class="abs fcol" style="left:251px">
  <h5>Information</h5>Faq<br>Terms &amp; Conditions<br>Privacy Policy
</div>
<div class="abs fcol" style="left:432px">
  <h5>Contact Info:</h5>14 Pelican Street<br>Coral Bay, Queensland<br>AUSTRALIA 4572<br><span>email:</span>admin@trimora.com.au
</div>
<div class="abs pay" aria-label="Accepted payment methods"><b></b><i></i><i></i><i></i><i></i></div>

<footer class="abs bottom">
  <div class="copyright">© Trimora 2014. All Rights Reserved.</div>
  <div class="follow">Follow us:</div>
  <i class="soc" style="left:823px"></i>
  <i class="soc" style="left:855px"></i>
</footer>

</body>
</html>
```